Lena Business card

This card is to represent me as a coach and Vivamora facilitator
Double sided in colour
A beautiful, simple and elegant design that indicates movement and is modern, FRESH and uplifting. Please don’t use much black and use the attached Vivamora logo.
Preferred colours - white, lighter blues and fresh greens

Target Market(s)
Business people - potential clients age 35 up
Industry/Entity Type
Business
Requirements
Must have
-  Text for the front :
Lumivera Living
Lena Darrow
Biocentric Coach
Co-Director, Vivamora School of Australia
E: lena@vivamora.com.au
M: 0471 552 908.
W: vivamora.com.au
Biocentric Coaching for Individuals, Teams and Organisations
Vivamora for Children, Adults and Social development projects
Text for the back :
The Vivamora system facilitates the expression of human potential for health, happiness and humanity through music, movement and group interaction. It was developed by Emilio Vasca Orduña, a Chilean anthropologist and clinical psychologist, in 1976.
Creative use of the logo - integrating it within the design - e.g perhaps using it as the O in Vivamora,
Please feature the heron from the logo or a another elegant graceful stylized heron.

```html
<!DOCTYPE html>
<html lang="en">
<head>
<meta charset="utf-8">
<title>Lena Darrow – Business Card</title>
<link href="https://fonts.googleapis.com/css2?family=Raleway:wght@300;400;500;600;700&display=swap" rel="stylesheet">
<style>
  :root {
    --page: #ffffff;
    --card: #504c52;
    --shadow: #a6a6a6;
    --teal: #3a9e94;
    --white: #ffffff;
    --soft-white: #e4e2e5;
    --dots: #d9d7da;
  }
  html, body {
    margin: 0;
    padding: 0;
    width: 1200px;
    height: 1000px;
    overflow: hidden;
    background: var(--page);
    font-family: "Raleway", Arial, sans-serif;
  }
  .canvas {
    position: relative;
    width: 1200px;
    height: 1000px;
  }
  .card {
    position: absolute;
    top: 42px;
    width: 521px;
    height: 913px;
    background: var(--card);
    box-shadow: 20px 18px 0 var(--shadow);
    color: var(--white);
    text-align: center;
  }
  .card--front { left: 47px; }
  .card--back { left: 625px; }

  .ribbon {
    position: absolute;
    left: 0;
    top: 0;
    width: 521px;
    height: 500px;
  }
  .brand-name {
    position: absolute;
    left: 141px;
    top: 190px;
    width: 242px;
    margin: 0;
    color: var(--white);
    font-weight: 600;
    font-size: 30px;
    line-height: 38px;
    text-align: center;
  }

  .divider {
    position: absolute;
    left: 53px;
    width: 415px;
    border-top: 3px dotted var(--dots);
  }

  .name {
    position: absolute;
    left: 0;
    width: 100%;
    top: 536px;
    margin: 0;
    font-size: 50px;
    font-weight: 700;
    letter-spacing: 0.5px;
  }
  .contact {
    position: absolute;
    top: 614px;
    left: 0;
    width: 100%;
    margin: 0;
    font-size: 20px;
    font-weight: 500;
    line-height: 26px;
  }
  .services {
    position: absolute;
    top: 765px;
    left: 0;
    width: 100%;
    margin: 0;
    font-size: 19px;
    font-weight: 300;
    line-height: 26px;
    color: var(--white);
  }
  .about {
    position: absolute;
    top: 564px;
    left: 20px;
    width: 481px;
    margin: 0;
    font-size: 23px;
    font-weight: 400;
    line-height: 30.4px;
  }
</style>
</head>
<body>
<div class="canvas">

  <section class="card card--front">
    <svg class="ribbon" viewBox="0 0 521 500" aria-hidden="true">
      <polygon points="141,0 383,0 383,490 262,416 141,490" fill="var(--teal)"/>
    </svg>
    <p class="brand-name">Lumivera<br>Living</p>

    <h1 class="name">LENA DARROW</h1>
    <div class="divider" style="top:604px"></div>
    <p class="contact">
      Biocentric Coach<br>
      Co-Director, Vivamora School of Australia<br>
      lena@vivamora.com.au<br>
      0471 552 908.<br>
      vivamora.com.au
    </p>
    <div class="divider" style="top:754px"></div>
    <p class="services">
      Biocentric Coaching for Individuals,<br>
      Teams and Organisations<br>
      Vivamora for Children, Adults<br>
      and Social development projects
    </p>
  </section>

  <section class="card card--back">
    <svg class="ribbon" viewBox="0 0 521 500" aria-hidden="true">
      <polygon points="141,0 383,0 383,490 262,416 141,490" fill="var(--teal)"/>
    </svg>
    <p class="brand-name">Lumivera<br>Living</p>

    <div class="divider" style="top:549px"></div>
    <p class="about">
      The Vivamora system<br>
      facilitates the expression of human<br>
      potential for health, happiness and<br>
      humanity through music,<br>
      movement and group interaction.<br>
      It was developed by Emilio Vasca<br>
      Orduña, a Chilean anthropologist<br>
      and clinical psychologist, in 1976.
    </p>
    <div class="divider" style="top:820px"></div>
  </section>

</div>
</body>
</html>
```